Food delivery wordpress design

need food delivery wordpress design for my site, here's the requirements
1. site must be pixel perfect , clean and professional
2. logo provided and must be match with the color scheme
3. pages : home , about us , faq , vendor registration

*** this is a information site no order can be made from the site, the site will show how things work , how to register as vendor , how to use the app , you may use any stock photo from pictorvane and send me the code, i will purchase it

you may use any of the logo to play with it

***** It must look scale and not looks like template where I can purchase elsewhere

the designer told me he can't work as he got his personal problem, please check his message

those who prefer to purchase online

Sans Serif

• refer to zelvo.com/my
• everything user and vendor like to know

```html
<!DOCTYPE html>
<html lang="en">
<head>
<meta charset="utf-8">
<title>makanmari — Food Delivery</title>
<link href="https://fonts.googleapis.com/css2?family=Poppins:wght@400;500;600;700&family=Oswald:wght@500;600&display=swap" rel="stylesheet">
<style>
:root{
  --orange:#F2A531;
  --orange-soft:#F6B44E;
  --dark:#232227;
  --ink:#2b2b2b;
  --heading:#4a4a4a;
  --white:#fff;
  --step-light:#fde7c2;
}
*{margin:0;padding:0;box-sizing:border-box}
html,body{width:1200px;height:4344px;overflow:hidden}
body{position:relative;background:var(--white);font-family:"Poppins",sans-serif;color:var(--ink)}
.abs{position:absolute}
a{color:inherit}

/* header */
.brand{left:93px;top:18px;display:flex;align-items:center;gap:10px}
.brand-dot{width:44px;height:44px;border-radius:50%;background:var(--orange)}
.brand-name{font-size:33px;font-weight:600;color:var(--heading);letter-spacing:-.5px}
.nav{top:38px;font-size:14px;font-weight:500;color:var(--ink)}
.nav-btn{left:952px;top:29px;width:152px;height:38px;border:2px solid var(--dark);background:var(--orange);font-size:13px;font-weight:500;display:flex;align-items:center;justify-content:center}

/* hero */
.hero-panel{left:0;top:86px;width:595px;height:588px;background:var(--orange)}
.hero-title{left:93px;top:232px;width:500px;font-size:53px;line-height:65px;font-weight:700;color:var(--white)}
.hero-mascot{left:649px;top:185px;width:463px;height:380px;background:linear-gradient(135deg,#fbe3b8,#f6f1ea)}

/* feature rows */
.feature-title{font-family:"Oswald",sans-serif;font-weight:600;font-size:37px;line-height:37px;letter-spacing:2px;color:var(--heading)}
.feature-text{font-size:15.5px;line-height:25.5px;color:var(--ink);width:205px}
.feature-link{font-size:16px;font-weight:500;text-decoration:underline}
.photo-stew{left:607px;top:831px;width:498px;height:345px;background:linear-gradient(135deg,#6b4a33,#a8673a 55%,#4a3222)}
.photo-groceries{left:98px;top:1289px;width:500px;height:344px;background:linear-gradient(135deg,#5d6a38,#3a3a38 50%,#b88a45)}

/* services */
.section-title{left:0;width:1200px;text-align:center;font-family:"Oswald",sans-serif;font-weight:600;font-size:37px;letter-spacing:2px;color:var(--heading)}
.section-sub{left:0;width:1200px;text-align:center;font-size:16px;letter-spacing:1px;font-weight:500}
.service{top:1890px;width:270px;text-align:center}
.service-photo{width:162px;height:162px;border-radius:50%;margin:0 auto}
.service-title{margin-top:47px;font-size:21px;font-weight:600;color:var(--orange)}
.service-text{margin-top:12px;font-size:13.5px;line-height:21px}
.service-mark{width:44px;height:44px;border-radius:50%;background:var(--orange);margin:22px auto 0}

/* order steps */
.order-photo{left:0;top:2620px;width:972px;height:641px;background:linear-gradient(135deg,#f3f2ee,#e8ebe3)}
.step{top:2538px;width:185px;height:161px;padding:25px 0 0 32px;color:var(--white)}
.step.orange{background:var(--orange-soft)}
.step.dark{background:var(--dark)}
.step-num{font-size:21px;font-weight:600}
.step-text{margin-top:14px;font-size:12.5px;line-height:16px;letter-spacing:.5px;width:130px}
.step.orange .step-text{color:var(--step-light)}

/* faq */
.faq{left:0;top:3262px;width:1200px;height:701px;background:var(--orange)}
.faq-title{left:0;top:3325px;width:1200px;text-align:center;font-size:24px;font-weight:600;letter-spacing:2px;color:var(--white)}
.faq-item{left:350px;width:499px;height:61px;background:var(--white);display:flex;align-items:center;justify-content:space-between;padding:0 22px;font-size:14.5px;letter-spacing:.5px;color:#333}

/* footer */
.footer{left:0;top:3963px;width:1200px;height:381px;background:var(--dark)}
.footer-brand{left:93px;top:4010px;display:flex;align-items:center;gap:10px}
.footer-about{left:93px;top:4078px;width:245px;font-size:11px;line-height:17.5px;color:var(--white)}
.footer-follow{left:93px;top:4179px;font-size:11px;color:var(--white)}
.socials{left:93px;top:4204px;display:flex;gap:5px}
.socials span{width:16px;height:16px;border-radius:50%;background:var(--orange)}
.footer-head{top:4001px;font-size:12.5px;color:var(--orange)}
.footer-list{left:401px;top:4034px;list-style:none;font-size:11px;color:var(--white)}
.footer-list li{height:27px;display:flex;align-items:center;gap:8px}
.footer-text{font-size:11px;line-height:17.5px;color:var(--white)}
.contact-row{left:593px;display:flex;gap:10px;font-size:11px;line-height:17.5px;color:var(--white)}
.news-input{left:843px;top:4039px;width:263px;height:41px;background:var(--orange);color:var(--dark);font-size:11px;font-weight:500;display:flex;align-items:center;gap:8px;padding-left:12px}
.news-btn{left:843px;top:4089px;width:263px;height:41px;background:var(--white);color:var(--dark);font-size:12px;font-weight:500;display:flex;align-items:center;justify-content:center}
.copyright{left:0;top:4298px;width:1200px;text-align:center;font-size:11px;font-weight:500;color:var(--white)}
.copyright b{color:var(--orange);font-weight:500}
</style>
</head>
<body>

<!-- header -->
<div class="abs brand"><span class="brand-dot"></span><span class="brand-name">makanmari</span></div>
<div class="abs nav" style="left:710px">Home</div>
<div class="abs nav" style="left:787px">About us</div>
<div class="abs nav" style="left:881px">Faq</div>
<div class="abs nav-btn">Vendor Registration</div>

<!-- hero -->
<div class="abs hero-panel"></div>
<h1 class="abs hero-title">Despite these uncertain times, we're still here to serve you</h1>
<div class="abs hero-mascot" role="img" aria-label="Mascot illustration of a running chef character"></div>

<!-- food delivery -->
<h2 class="abs feature-title" style="left:93px;top:888px">FOOD<br>DELIVERY</h2>
<p class="abs feature-text" style="left:300px;top:882px">Get your comfort food from your favourite restaurant without leaving home. Order via the Zelvo app, or click below to order from our website.</p>
<a class="abs feature-link" style="left:300px;top:1074px">Order via website</a>
<div class="abs photo-stew" role="img" aria-label="Photo of a spicy tofu stew in a golden pot with rice"></div>

<!-- groceries -->
<div class="abs photo-groceries" role="img" aria-label="Photo of fresh vegetables and grains around a dark slate"></div>
<h2 class="abs feature-title" style="left:674px;top:1352px">GROCERIES</h2>
<p class="abs feature-text" style="left:881px;top:1349px">Get your comfort food from your favourite restaurant without leaving home. Order via the Zelvo app, or click below to order from our website.</p>
<a class="abs feature-link" style="left:891px;top:1540px">Download the</a>

<!-- services -->
<h2 class="abs section-title" style="top:1741px">ALL THE SERVICES</h2>
<p class="abs section-sub" style="top:1792px">Your favourite food delivered hot and fresh</p>

<div class="abs service" style="left:69px">
  <div class="service-photo" role="img" aria-label="Photo of grilled skewers on a plate" style="background:linear-gradient(135deg,#b4583e,#3e2c26)"></div>
  <div class="service-title">Just a tap away.</div>
  <p class="service-text">Get your comfort food from<br>your favourite restaurant<br>without leaving home.<br>Order via the Zelvo app, or<br>click below to order from</p>
  <div class="service-mark" role="img" aria-label="Small mascot icon"></div>
</div>
<div class="abs service" style="left:338px">
  <div class="service-photo" role="img" aria-label="Photo of falafel with fresh salad" style="background:linear-gradient(135deg,#b57e3a,#5a7a3a)"></div>
  <div class="service-title">Foods for all cravings.</div>
  <p class="service-text">Get your comfort food from<br>your favourite restaurant<br>without leaving home.<br>Order via the Zelvo app, or<br>click below to order from</p>
  <div class="service-mark" role="img" aria-label="Small mascot icon"></div>
</div>
<div class="abs service" style="left:586px">
  <div class="service-photo" role="img" aria-label="Photo of a card payment terminal" style="background:linear-gradient(135deg,#8e959c,#cdbc9c)"></div>
  <div class="service-title">Pay with ease.</div>
  <p class="service-text">Get your comfort food from<br>your favourite restaurant<br>without leaving home.<br>Order via the Zelvo app, or<br>click below to order from</p>
  <div class="service-mark" role="img" aria-label="Small mascot icon"></div>
</div>
<div class="abs service" style="left:856px">
  <div class="service-photo" role="img" aria-label="Illustration of a reward trophy celebration" style="background:linear-gradient(135deg,#f7f4ee,#f3e2bd);box-shadow:0 0 0 1px #eee"></div>
  <div class="service-title">It's more rewarding.</div>
  <p class="service-text">Get your comfort food from<br>your favourite restaurant<br>without leaving home.<br>Order via the Zelvo app, or<br>click below to order from</p>
  <div class="service-mark" role="img" aria-label="Small mascot icon"></div>
</div>

<!-- make an order -->
<h2 class="abs section-title" style="top:2455px">MAKE AN ORDER</h2>
<div class="abs order-photo" role="img" aria-label="Photo of a hand holding a phone with the ordering app, surrounded by salmon, vegetables and pasta"></div>
<div class="abs step orange" style="left:98px"><div class="step-num">01</div><p class="step-text">Launch the Zelvo app and saelect "Food"</p></div>
<div class="abs step dark" style="left:300px"><div class="step-num">02</div><p class="step-text">Enter your delivery address.</p></div>
<div class="abs step orange" style="left:504px"><div class="step-num">03</div><p class="step-text">Select your favourite restaurant.</p></div>
<div class="abs step dark" style="left:708px"><div class="step-num">04</div><p class="step-text">Launch the Zelvo app and saelect "Food"</p></div>
<div class="abs step orange" style="left:908px"><div class="step-num">05</div><p class="step-text">Launch the Zelvo app and saelect "Food"</p></div>

<!-- faq -->
<div class="abs faq"></div>
<h2 class="abs faq-title">FAQs</h2>
<div class="abs faq-item" style="top:3390px"><span>Lorem Ipsum is simply dummy&nbsp; text of ?</span><svg width="16" height="10" viewBox="0 0 16 10"><path d="M1 1l7 7 7-7" fill="none" stroke="#aaa" stroke-width="1.5"/></svg></div>
<div class="abs faq-item" style="top:3466px"><span>Printing and typesetting induastry?</span><svg width="16" height="10" viewBox="0 0 16 10"><path d="M1 1l7 7 7-7" fill="none" stroke="#aaa" stroke-width="1.5"/></svg></div>
<div class="abs faq-item" style="top:3545px"><span>Ipsum has been the industry's?</span><svg width="16" height="10" viewBox="0 0 16 10"><path d="M1 1l7 7 7-7" fill="none" stroke="#aaa" stroke-width="1.5"/></svg></div>
<div class="abs faq-item" style="top:3624px"><span>Dummy text ever since the ?</span><svg width="16" height="10" viewBox="0 0 16 10"><path d="M1 1l7 7 7-7" fill="none" stroke="#aaa" stroke-width="1.5"/></svg></div>
<div class="abs faq-item" style="top:3704px"><span>When an unknown printer took?</span><svg width="16" height="10" viewBox="0 0 16 10"><path d="M1 1l7 7 7-7" fill="none" stroke="#aaa" stroke-width="1.5"/></svg></div>
<div class="abs faq-item" style="top:3781px"><span>Galley of type and scrambled ?</span><svg width="16" height="10" viewBox="0 0 16 10"><path d="M1 1l7 7 7-7" fill="none" stroke="#aaa" stroke-width="1.5"/></svg></div>

<!-- footer -->
<div class="abs footer"></div>
<div class="abs footer-brand"><span class="brand-dot"></span><span class="brand-name">makanmari</span></div>
<p class="abs footer-about">Lorem Ipsum is simply dummy text of the printing and typesetting industry. Lorem Ipsum has been the industry's standard dummy text ever since the 1500s, when an unknown printer</p>
<div class="abs footer-follow">Follow us on</div>
<div class="abs socials" aria-label="Social links"><span></span><span></span><span></span><span></span></div>

<div class="abs footer-head" style="left:401px">Our Services</div>
<ul class="abs footer-list">
  <li><svg width="16" height="10" viewBox="0 0 16 10"><path d="M0 5h14M10 1l4 4-4 4" fill="none" stroke="#fff" stroke-width="1.3"/></svg>Lorem Ipsum is</li>
  <li><svg width="16" height="10" viewBox="0 0 16 10"><path d="M0 5h14M10 1l4 4-4 4" fill="none" stroke="#fff" stroke-width="1.3"/></svg>Simply dummy</li>
  <li><svg width="16" height="10" viewBox="0 0 16 10"><path d="M0 5h14M10 1l4 4-4 4" fill="none" stroke="#fff" stroke-width="1.3"/></svg>Text of the</li>
  <li><svg width="16" height="10" viewBox="0 0 16 10"><path d="M0 5h14M10 1l4 4-4 4" fill="none" stroke="#fff" stroke-width="1.3"/></svg>Printing and</li>
  <li><svg width="16" height="10" viewBox="0 0 16 10"><path d="M0 5h14M10 1l4 4-4 4" fill="none" stroke="#fff" stroke-width="1.3"/></svg>Typesetting</li>
  <li><svg width="16" height="10" viewBox="0 0 16 10"><path d="M0 5h14M10 1l4 4-4 4" fill="none" stroke="#fff" stroke-width="1.3"/></svg>Industry. Lorem</li>
</ul>

<div class="abs footer-head" style="left:593px">Company Address</div>
<p class="abs footer-text" style="left:593px;top:4032px;width:215px">Porem awesome dolor sitework amet, consetur acing elit, sed do eiusmod ligol</p>
<div class="abs contact-row" style="top:4097px"><svg width="18" height="18" viewBox="0 0 18 18"><path d="M16 2L2 8l6 2 2 6z" fill="none" stroke="#F2A531" stroke-width="1.3"/></svg><span>Address: 12/7 Larkfield Row,<br>Ternhollow.</span></div>
<div class="abs contact-row" style="top:4153px"><svg width="18" height="18" viewBox="0 0 18 18"><path d="M4 2l3 0 1 4-2 1c1 2 3 4 5 5l1-2 4 1v3c-7 1-13-5-12-12z" fill="none" stroke="#F2A531" stroke-width="1.3"/></svg><span>Phone: 55501234567</span></div>
<div class="abs contact-row" style="top:4187px"><svg width="18" height="18" viewBox="0 0 18 18"><rect x="2" y="4" width="14" height="10" fill="none" stroke="#F2A531" stroke-width="1.3"/><path d="M2 4l7 6 7-6" fill="none" stroke="#F2A531" stroke-width="1.3"/></svg><span>Email:hello@makanmari.com</span></div>

<div class="abs footer-head" style="left:843px">Newsletter</div>
<div class="abs news-input"><svg width="16" height="16" viewBox="0 0 18 18"><path d="M16 2L2 8l6 2 2 6z" fill="none" stroke="#232227" stroke-width="1.3"/></svg>Enter your email id :</div>
<div class="abs news-btn">Submit Now</div>

<div class="abs copyright">Copyright © 2021 <b>Makanmari</b></div>

</body>
</html>
```